Real Estate Sign - For Sale Yard Sign - Willowmere Estates

Our real estate company is looking for a new sign design to hang from in post in the front yard of the homes we are selling. Our company name is Willowmere Estates and we are open to any ideas. Attached for you is our company logo and name. The font is Trajan Pro. We are looking for a classy sign to put in front of our high end more expensive homes. You can either choose to include or not include the words "FOR SALE" on the sign (in our state, only about 1/2 of the real estate signs have room for those words. It is implied with a sign in the yard in front of a home). Thank you.

24 inches wide is important. and the height should be either 18, 24 or 30 inches. For printing purposes either of those heights will work. 18 inches is common, but some signs look great that are taller too. I'm open.

If you have any ideas for some better text options, styles or fonts, feel free to play with it.

P.S. Please feel free to play with the colors. We are not at this point set on a particular color scheme. Colors we think are nice but you may have other better ideas are black, red, white, gold, green

Target Market(s)

High end real estate home owners who choose to use our company to sell their home.

Industry/Entity Type

Real Estate

Requirements
Must have
• Company Logo
Company Name (Willowmere Estates)
Barnaby Follwick (please include my name as I am the real estate agent)
503-618-3940 (my phone number for potential clients to contact me)
Website name - willowmereestatesnw.example
***You can either choose to include the words "FOR SALE" or not***

Dimensions must be 24 inches wide. Height can be either 18, 24 or 30 inches. Must be one of those 3 heights for printing purposes.

```html
<!DOCTYPE html>
<html lang="en">
<head>
<meta charset="utf-8">
<title>Willowmere Estates – Yard Sign</title>
<link href="https://fonts.googleapis.com/css2?family=Cinzel:wght@400&family=Tinos&display=swap" rel="stylesheet">
<style>
  :root {
    --page: #ffffff;
    --frame: #0a0a0a;
    --panel: #e3e8e5;
    --ink: #111111;
    --accent-red: #fe0a0a;
    --on-red: #ffffff;
    --shadow: rgba(0, 0, 0, 0.55);
  }
  * { box-sizing: border-box; margin: 0; padding: 0; }
  html, body {
    width: 1200px;
    height: 1000px;
    overflow: hidden;
    background: var(--page);
  }
  .canvas {
    position: relative;
    width: 1200px;
    height: 1000px;
  }
  .yard-sign {
    position: absolute;
    left: 93px;
    top: 115px;
    width: 1014px;
    height: 770px;
    background: var(--frame);
    box-shadow: 12px 14px 8px var(--shadow);
  }
  .sign-face {
    position: absolute;
    left: 20px;
    top: 20px;
    width: 974px;
    height: 729px;
    background: var(--panel);
  }
  .brand-name {
    position: absolute;
    left: 0;
    width: 100%;
    top: 90px;
    text-align: center;
    font-family: "Cinzel", "Trajan Pro", serif;
    font-weight: 400;
    color: var(--ink);
    line-height: 1;
  }
  .brand-name .primary {
    display: block;
    font-size: 104px;
    letter-spacing: 0.01em;
  }
  .brand-name .secondary {
    display: block;
    margin-top: 20px;
    font-size: 54px;
    letter-spacing: 0.08em;
  }
  .website {
    position: absolute;
    left: 0;
    width: 100%;
    top: 315px;
    text-align: center;
    font-family: "Tinos", "Times New Roman", serif;
    font-size: 60px;
    color: var(--ink);
    line-height: 1;
  }
  .agent-band {
    position: absolute;
    left: 0;
    top: 400px;
    width: 100%;
    height: 200px;
    background: var(--accent-red);
    color: var(--on-red);
    font-family: "Tinos", "Times New Roman", serif;
    text-align: center;
    line-height: 1;
  }
  .agent-name {
    position: absolute;
    left: 0;
    width: 100%;
    top: 24px;
    font-size: 72px;
  }
  .agent-phone {
    position: absolute;
    left: 0;
    width: 100%;
    top: 112px;
    font-size: 84px;
  }
</style>
</head>
<body>
  <div class="canvas">
    <div class="yard-sign">
      <div class="sign-face">
        <h1 class="brand-name">
          <span class="primary">WILLOWMERE</span>
          <span class="secondary">Estates Real Estate</span>
        </h1>
        <p class="website">willowmereestatesnw.example</p>
        <div class="agent-band">
          <p class="agent-name">Barnaby Follwick</p>
          <p class="agent-phone">503-618-3940</p>
        </div>
      </div>
    </div>
  </div>
</body>
</html>
```